A Freight forwarding (transportation/shipping) company requires stationary designs

We need The following:
1. Letterhead
2. Letter Envelope
3. Business Card Design
4. A4 Paper Envelope
5. A4 Paper Folder (One that is 2xA4 foldable size which we can open in half and we can put a paper in between and has a lot for business card)
6. A5 Paper (To be used for notes taking)
a design for a freight forwarding company named KORVALE DIMAS INTERNATIONAL TRANSPORTATION.
(We are active in Sea Transportation, Truck transportation, and Air Transportation, (printed design in PDF is required with all open source files for editing - lamination accepted)
Playing around with the Logo is accepted,, Korvale Logo.png is the correct logo.
Example of folder, envelopes, and notepad attached
Address of the company is :
No 7, 4th Tarvandi Gharbi, Nasim Dareh Blvd,
Mashhad, IR
Tel : +98 51 30000000
Fax : +98 51 30000001
Website : www.korvale-example.com
Email : info@korvale-example.com

```html
<!DOCTYPE html>
<html lang="en">
<head>
<meta charset="utf-8">
<title>Korvale Dimas – Business Card</title>
<link href="https://fonts.googleapis.com/css2?family=PT+Sans:wght@400;700&display=swap" rel="stylesheet">
<style>
  :root {
    --page-bg: #e6e7ea;
    --card-bg: #f4f5f6;
    --navy: #282a78;
    --green: #2e7a3c;
    --text: #3a3a3a;
    --band-text: #9aa0c4;
    --rule: #8c8f99;
  }
  html, body {
    margin: 0;
    padding: 0;
    width: 1200px;
    height: 969px;
    overflow: hidden;
    background: var(--page-bg);
    font-family: "PT Sans", Arial, sans-serif;
  }
  .canvas {
    position: relative;
    width: 1200px;
    height: 969px;
  }
  .business-card {
    position: absolute;
    left: 100px;
    top: 199px;
    width: 1000px;
    height: 571px;
    background: var(--card-bg);
    overflow: hidden;
    box-shadow: 0 6px 24px rgba(0,0,0,0.15);
  }
  .card-band {
    position: absolute;
    inset: 0;
    width: 1000px;
    height: 571px;
  }
  .brand-mark {
    position: absolute;
    left: 147px;
    top: 102px;
    width: 234px;
    height: 234px;
  }
  .brand-name {
    position: absolute;
    left: 44px;
    width: 440px;
    top: 338px;
    text-align: center;
    font-size: 34px;
    font-weight: 400;
    color: var(--navy);
    letter-spacing: 0.5px;
    margin: 0;
  }
  .divider {
    position: absolute;
    left: 440px;
    top: 124px;
    width: 2px;
    height: 293px;
    background: var(--rule);
  }
  .contact {
    position: absolute;
    left: 497px;
    top: 110px;
  }
  .contact-name {
    margin: 0;
    font-size: 31px;
    font-weight: 700;
    color: var(--navy);
    line-height: 1;
  }
  .contact-title {
    margin: 10px 0 0;
    font-size: 27px;
    color: var(--green);
    line-height: 1;
  }
  .contact-address {
    margin: 16px 0 0;
    font-size: 25px;
    line-height: 36px;
    color: var(--text);
    font-style: normal;
  }
  .contact-lines {
    list-style: none;
    margin: 0;
    padding: 0;
    font-size: 25px;
    line-height: 34px;
    color: var(--text);
  }
  .contact-lines li {
    display: flex;
    align-items: center;
    gap: 12px;
  }
  .contact-icon {
    width: 20px;
    height: 20px;
    fill: var(--navy);
    flex: none;
  }
  .website {
    position: absolute;
    left: 0;
    width: 1000px;
    top: 526px;
    text-align: center;
    font-size: 24px;
    letter-spacing: 9px;
    color: var(--band-text);
  }
</style>
</head>
<body>
<div class="canvas">
  <div class="business-card">
    <svg class="card-band" viewBox="0 0 1000 571" aria-hidden="true">
      <path d="M0,537 Q500,478 1000,552 L1000,571 L0,571 Z" fill="var(--navy)"/>
      <path d="M0,528 Q500,468 1000,543" fill="none" stroke="var(--green)" stroke-width="4"/>
    </svg>

    <svg class="brand-mark" viewBox="0 0 234 234" aria-hidden="true">
      <circle cx="117" cy="117" r="110" fill="none" stroke="var(--navy)" stroke-width="12"/>
    </svg>
    <p class="brand-name">KORVALE DIMAS</p>

    <div class="divider"></div>

    <div class="contact">
      <h1 class="contact-name">DAREN HOLLOWAY</h1>
      <p class="contact-title">CEO/FOUNDER</p>
      <address class="contact-address">
        No 7, 4th Tarvandi Gharbi<br>
        Nasim Dareh Blvd,<br>
        Mashhad, IR
      </address>
      <ul class="contact-lines">
        <li>
          <svg class="contact-icon" viewBox="0 0 24 24" aria-hidden="true"><path d="M6.6 10.8a15.1 15.1 0 0 0 6.6 6.6l2.2-2.2c.3-.3.7-.4 1-.2 1.1.4 2.3.6 3.6.6.6 0 1 .4 1 1V20c0 .6-.4 1-1 1A17 17 0 0 1 3 4c0-.6.4-1 1-1h3.5c.6 0 1 .4 1 1 0 1.3.2 2.5.6 3.6.1.3 0 .7-.2 1z"/></svg>
          +98 51 30000000
        </li>
        <li>
          <svg class="contact-icon" viewBox="0 0 24 24" aria-hidden="true"><path d="M6 2h10l2 2v5H6zM3 10h18a1 1 0 0 1 1 1v8a1 1 0 0 1-1 1h-3v-4H6v4H3a1 1 0 0 1-1-1v-8a1 1 0 0 1 1-1zm5 8h8v4H8z"/></svg>
          +98 51 30000001
        </li>
        <li>
          <svg class="contact-icon" viewBox="0 0 24 24" aria-hidden="true"><path d="M2 5h20v14H2zm2 2v.5l8 5 8-5V7l-8 5z"/></svg>
          info@korvale-example.com
        </li>
      </ul>
    </div>

    <div class="website">www.korvale-example.com</div>
  </div>
</div>
</body>
</html>
```